website design for Company KMV

Our company name KMV(the civic canvas limited), need design a website. It is a website that focuses on promoting art design in the world.
We will provide the existing logo design, the new website and logo should be matched to each other. The website has to include pages "Home" "Contact" "Service" and So on at least 6-8 pages. The site is mainly for publicity and promotion. We will have an existing domain and hosting.
Updates

We prefer the original design, thanks.

Target Market(s)

large public art

Industry/Entity Type

Architecture and design, large public art and sculpture manufacturer

Coding

Coded - Design and coding required

Number of Pages Required

5+ page

Requirements
Must have
• 1. the overall color has to match our logo color 2. Do not need to do any change on our logo including the color 3. Here is a similar style of the home page we like, it can be similar but must not same. Pls check the below link. https://www.darveno.example/en-us/

```html
<!DOCTYPE html>
<html lang="en">
<head>
<meta charset="utf-8">
<title>KMV — The Civic Canvas Limited</title>
<link href="https://fonts.googleapis.com/css2?family=Exo+2:wght@400;500;600&family=Montserrat:wght@400;500;600;700&display=swap" rel="stylesheet">
<style>
:root{
  --orange:#fb8a2b;
  --ink:#1c1c1c;
  --grey:#555658;
  --dark:#2a2b2d;
  --darker:#1d1e20;
  --slate:#5b5c5f;
  --white:#ffffff;
  --muted:#565656;
}
*{margin:0;padding:0;box-sizing:border-box}
html,body{width:1200px;height:3431px;overflow:hidden}
body{position:relative;background:var(--white);font-family:"Montserrat",sans-serif;color:var(--ink)}
.abs{position:absolute}
.btn{position:absolute;width:208px;height:75px;border-radius:38px;background:var(--orange);color:var(--white);font:700 15px "Montserrat",sans-serif;display:flex;align-items:center;justify-content:center;letter-spacing:.2px}
.display{font-family:"Exo 2",sans-serif;font-weight:500;letter-spacing:2px;text-transform:uppercase}
.display .soft{color:var(--grey)}

/* header */
.site-header{left:0;top:0;width:1200px;height:88px;background:var(--white)}
.brand{left:144px;top:20px;display:flex;align-items:center;gap:10px;font:600 30px "Exo 2",sans-serif;color:var(--ink);letter-spacing:1px}
.brand small{font-size:17px;letter-spacing:1.5px;line-height:1.05;text-transform:uppercase;font-weight:600;width:190px}
.nav{left:585px;top:36px;display:flex;gap:25px;font:600 13px "Montserrat",sans-serif;color:var(--ink)}
.nav .active{position:relative}
.nav .active::after{content:"";position:absolute;left:0;right:0;top:22px;height:3px;background:var(--orange)}
.cart{left:1036px;top:36px}

/* hero */
.hero{left:0;top:88px;width:1200px;height:542px;background:linear-gradient(120deg,#c8283a 0%,#1f3a4a 30%,#d4345a 45%,#2f8a5a 60%,#e0a91f 78%,#c4882a 100%)}
.hero-title{left:148px;top:190px;font:600 64px/78px "Exo 2",sans-serif;color:var(--white);letter-spacing:2px}
.hero-dots{left:1124px;top:294px;display:flex;flex-direction:column;gap:13px}
.hero-dots i{width:8px;height:8px;border-radius:50%;background:var(--white)}
.hero-dots i.on{background:#4aa3df}

/* about */
.about-mark{left:150px;top:680px;font:600 140px/1 "Exo 2",sans-serif;color:var(--ink);letter-spacing:4px}
.section-title{font-size:50px}
.body-copy{font-size:13.3px;line-height:24.8px;color:var(--muted)}

/* service */
.service{left:0;top:1128px;width:1200px;height:574px;background:var(--dark)}
.service-copy{color:#e6e6e6}

/* products */
.product{position:absolute;top:1936px;width:208px;text-align:center}
.product .frame{width:208px;height:152px;border:6px solid #8a5a3a;box-shadow:0 2px 4px rgba(0,0,0,.35)}
.product h3{margin-top:27px;font:600 16px "Montserrat",sans-serif;color:#222}
.product p{margin-top:11px;font:700 18px "Montserrat",sans-serif;color:var(--orange)}

/* gallery */
.tile{position:absolute;width:292px;height:249px}

/* footer */
.footer{left:0;top:3081px;width:1200px;height:350px;background:var(--dark);color:var(--white)}
.footer h4{font:700 19px "Montserrat",sans-serif;letter-spacing:.5px}
.footer .small{font-size:12px;line-height:18px;color:#e2e2e2}
.links li{list-style:none;font-size:12px;color:#e2e2e2;height:21px}
.links li::before{content:"»";margin-right:10px}
.ci-row{display:flex;align-items:center;gap:14px;margin-bottom:14px}
.ci-icon{width:32px;height:32px;border-radius:50%;border:1.5px solid #ddd;flex:none;display:flex;align-items:center;justify-content:center}
</style>
</head>
<body>

<header class="abs site-header">
  <div class="abs brand">KMV <small>The Civic Canvas</small></div>
  <nav class="abs nav">
    <span class="active">HOME</span><span>ABOUT</span><span>ARTS</span><span>CONTACT</span><span>NEWS</span><span>SERVICES</span>
  </nav>
  <svg class="abs cart" width="18" height="16" viewBox="0 0 18 16"><path d="M0 1h3l2.5 9h9L17 3H5" fill="none" stroke="#1c1c1c" stroke-width="2"/><rect x="5" y="3" width="11" height="6" fill="#1c1c1c"/><circle cx="7" cy="13.5" r="1.6" fill="#1c1c1c"/><circle cx="14" cy="13.5" r="1.6" fill="#1c1c1c"/></svg>
</header>

<section class="abs hero" role="img" aria-label="Close-up of swirling multicoloured fluid paint artwork"></section>
<h1 class="abs hero-title">THE CIVIC CANVAS<br>LIMITED</h1>
<a class="btn" style="left:149px;top:381px">GET STARTED</a>
<div class="abs hero-dots"><i></i><i class="on"></i><i></i><i></i></div>
<svg class="abs" style="left:0;top:578px" width="1200" height="53"><polygon points="140,0 1059,0 1076,53 124,53" fill="#fff"/></svg>

<div class="abs about-mark">KMV</div>
<h2 class="abs display section-title" style="left:600px;top:666px">About <span class="soft">KMV</span></h2>
<p class="abs body-copy" style="left:601px;top:749px;width:440px">Lorem ipsum dolor sit amet, consectetur adipiscing elit, sed do eiusmod tempor incididunt ut labore et dolore magna aliquis ipsum suspendisse ultrices gravids cLorem ipsum dolor sit amet, consectetur adipiscing elit, sed do eiusmod tempor incididunt ut labore et dolore magna aliquis ipsum suspendisse ultrices gravids commodo viverra maecenas accumsan lacus vel facilimmodo viverra maecenas accumsan lacus vel facilisis.</p>
<a class="btn" style="left:601px;top:958px">READ MORE</a>

<section class="abs service">
  <svg class="abs" style="left:0;top:0" width="1200" height="574">
    <polygon points="533,0 1200,0 1200,574 713,574" fill="#fff"/>
    <polygon points="540,0 1200,0 1200,574 720,574" fill="url(#studio)" role="img" aria-label="Artist painting a large canvas in a studio"/>
    <defs><linearGradient id="studio" x1="0" y1="0" x2="1" y2="0.3"><stop offset="0" stop-color="#6f9fb0"/><stop offset=".35" stop-color="#c86a4a"/><stop offset=".7" stop-color="#b98a4a"/><stop offset="1" stop-color="#e0a24a"/></linearGradient></defs>
  </svg>
  <h2 class="abs display section-title" style="left:143px;top:100px;color:#fff">Service</h2>
  <p class="abs body-copy service-copy" style="left:143px;top:180px;width:445px">Lorem ipsum dolor sit amet, consectetur adipiscing elit, sed do eiusmod tempor incididunt ut labore et dolore magna aliquis ipsum suspendisse ultrices gravids cLorem ipsum dolor sit amet, consectetur adipiscing elit, sed do eiusmod tempor incididunt ut labore et dolore magna aliquis ipsum suspendisse ultrices gravids commodo viverra maecenas accumsan lacus vel facilimmodo viverra maecenas accumsan lacus vel facilisis.</p>
  <a class="btn" style="left:143px;top:390px">READ MORE</a>
</section>

<h2 class="abs display section-title" style="left:0;width:1200px;text-align:center;top:1812px;font-size:54px">Featured <span class="soft">Arts</span></h2>
<div class="product" style="left:145px"><div class="frame" role="img" aria-label="Abstract geometric painting" style="background:linear-gradient(135deg,#3ab0a0,#d8502a,#2a7ac0)"></div><h3>PRODUCT NAME</h3><p>$56.87</p></div>
<div class="product" style="left:380px"><div class="frame" role="img" aria-label="Painting of autumn trees" style="background:linear-gradient(160deg,#8ab0d0,#e08a2a,#c04a1a,#6a8a3a)"></div><h3>PRODUCT NAME</h3><p>$56.87</p></div>
<div class="product" style="left:614px"><div class="frame" role="img" aria-label="Painting of a leaping figure" style="background:linear-gradient(150deg,#a0c8e8,#6a5ac0,#d05a8a)"></div><h3>PRODUCT NAME</h3><p>$56.87</p></div>
<div class="product" style="left:848px"><div class="frame" role="img" aria-label="Blue abstract palette-knife painting" style="background:linear-gradient(135deg,#1a4ac0,#3aa0e0,#1a2a90)"></div><h3>PRODUCT NAME</h3><p>$56.87</p></div>
<a class="btn" style="left:496px;top:2228px">VIEW MORE</a>

<div class="tile" role="img" aria-label="Fluid art in red and blue" style="left:0;top:2381px;background:linear-gradient(135deg,#e03a2a,#f0c020,#2aa0e0)"></div>
<div class="tile" role="img" aria-label="Abstract brushstroke art" style="left:302px;top:2381px;background:linear-gradient(135deg,#2a6a5a,#c04a6a,#3a8ad0)"></div>
<div class="tile" role="img" aria-label="Fluid art in blue tones" style="left:605px;top:2381px;background:linear-gradient(135deg,#e02a3a,#2a6ae0,#9ac0e0)"></div>
<div class="tile" role="img" aria-label="Fluid art in purple and teal" style="left:908px;top:2381px;background:linear-gradient(135deg,#5a2a6a,#c03a6a,#2ab0c0)"></div>
<div class="tile" role="img" aria-label="Fluid art in red and black" style="left:0;top:2640px;background:linear-gradient(135deg,#2a6ae0,#e0202a,#1a1a2a)"></div>
<div class="tile" role="img" aria-label="Layered multicolour paint art" style="left:302px;top:2640px;background:linear-gradient(135deg,#2a8a9a,#d06a2a,#e04a2a)"></div>
<div class="tile" role="img" aria-label="Marbled purple and white art" style="left:605px;top:2640px;background:linear-gradient(135deg,#3a1a4a,#e8e0f0,#6a1a5a)"></div>
<div class="tile" role="img" aria-label="Fluid art in blue and red" style="left:908px;top:2640px;background:linear-gradient(135deg,#2a8ae0,#e02a2a,#1a4ac0)"></div>
<a class="btn" style="left:496px;top:2942px">VIEW MORE</a>

<footer class="abs footer">
  <svg class="abs" style="left:0;top:0" width="1200" height="350">
    <polygon points="0,0 143,0 0,350" fill="#1d1e20"/>
    <polygon points="1057,0 1200,0 1200,350" fill="#5b5c5f"/>
  </svg>
  <h4 class="abs" style="left:143px;top:78px">NEWSLETTER SUBSCRIBE</h4>
  <p class="abs small" style="left:143px;top:118px">Sed ut perspiciatis unde omnis iste natus error luptatem..</p>
  <div class="abs" style="left:144px;top:165px;width:230px;height:36px;background:#fff;color:#555;font-size:12px;padding:11px 18px">Enter Email</div>
  <div class="abs" style="left:374px;top:165px;width:109px;height:36px;background:var(--orange);font:600 13px Montserrat,sans-serif;display:flex;align-items:center;justify-content:center">SUBSCRIBE</div>
  <div class="abs" style="left:146px;top:238px;display:flex;gap:8px">
    <i style="width:25px;height:25px;border-radius:50%;background:#3b5a9a"></i>
    <i style="width:25px;height:25px;border-radius:50%;background:#2aa0e0"></i>
    <i style="width:25px;height:25px;border-radius:50%;background:#d6342a"></i>
    <i style="width:25px;height:25px;border-radius:50%;background:#8a6a4a"></i>
    <i style="width:25px;height:25px;border-radius:50%;background:#c01a2a"></i>
    <i style="width:25px;height:25px;border-radius:50%;background:#f07a1a"></i>
  </div>

  <h4 class="abs" style="left:571px;top:78px">CONTACT INFO</h4>
  <div class="abs small" style="left:571px;top:121px;width:300px">
    <div class="ci-row"><span class="ci-icon"><svg width="12" height="14" viewBox="0 0 12 14"><path d="M6 13S1 8 1 5a5 5 0 0 1 10 0c0 3-5 8-5 8z" fill="none" stroke="#fff" stroke-width="1.4"/><circle cx="6" cy="5" r="1.7" fill="#fff"/></svg></span><span>233,Sed ut perspiciatis unde omnis<br>iste natus error luptatem..</span></div>
    <div class="ci-row"><span class="ci-icon"><svg width="12" height="12" viewBox="0 0 12 12"><path d="M2 1l2 0 1 3-1.5 1a7 7 0 0 0 3.5 3.5L8 7l3 1v2a1 1 0 0 1-1 1A9 9 0 0 1 1 2a1 1 0 0 1 1-1z" fill="#fff"/></svg></span><span>Phone: 1 555 010 0199</span></div>
    <div class="ci-row"><span class="ci-icon"><svg width="13" height="10" viewBox="0 0 13 10"><rect x=".5" y=".5" width="12" height="9" fill="#fff"/><path d="M.5 .5l6 5 6-5" fill="none" stroke="#2a2b2d"/></svg></span><span>Email: info@civiccanvas.example</span></div>
  </div>

  <h4 class="abs" style="left:923px;top:78px">QUICK LINKS</h4>
  <ul class="abs links" style="left:923px;top:120px">
    <li>Home</li><li>About us</li><li>Services</li><li>Products</li><li>News</li><li>Contact us</li>
  </ul>

  <div class="abs" style="left:143px;top:291px;width:914px;height:1px;background:#444"></div>
  <p class="abs small" style="left:143px;top:309px;font-size:11.5px">Copyrights © 2021,KMV.All Rights Reserved.&nbsp; | &nbsp;Privacy policy</p>
  <div class="abs" style="left:902px;top:304px;width:154px;height:27px;background:#fff;display:flex;gap:3px;padding:3px">
    <i style="flex:1;background:#1a2a8a"></i><i style="flex:1;background:#e03a2a"></i><i style="flex:1;background:#2a7ac0"></i><i style="flex:1.6;background:#1a5ab0"></i>
  </div>
</footer>

</body>
</html>
```